Business Card, A4 Letter Head and DL Envelope for Vantrelle

We are looking for a design for our Business Card, A4 Letter Head and DL Envelope.

Vantrelle is a distributor of promotional products. We specialize in a range of branded promotional products, these include pens, polo shirts, key rings, drink bottles, uniforms and bags to name a few. We are experts in marketing and assist companies in choosing the right promotional product for their needs. We will predominately be an online business where customers visit our website and browse our range of promotional products and branding options.

Our colours are black, red, white and grey.

Files must be supplied in eps, pdf and ai format.

Please display the following information:
Corbin Hale
Account Manager
Suite xxx, 214 Dawlish Parade Melbourne, Victoria 3000
Phone +61 3 5550 1827
Mobile +61 455 501 936
sales@vantrelle.com.au
www.vantrelle.com.au

```html
<!DOCTYPE html>
<html lang="en">
<head>
<meta charset="utf-8">
<title>Vantrelle — Business Card</title>
<link rel="stylesheet" href="https://fonts.googleapis.com/css2?family=Tinos:wght@700&family=Arimo:wght@700&display=swap">
<style>
  :root {
    --ink-black: #000000;
    --fade-grey: #d9d9d9;
    --paper-white: #ffffff;
    --brand-red: #e0000e;
    --deep-red: #b10008;
    --lower-grey: #c9c9c9;
    --shadow-dark: rgba(0, 0, 0, 0.75);
  }
  html, body {
    margin: 0;
    padding: 0;
    width: 1200px;
    height: 741px;
    overflow: hidden;
    background: var(--paper-white);
  }
  .card {
    position: relative;
    width: 1200px;
    height: 741px;
    overflow: hidden;
    background: linear-gradient(to bottom, var(--ink-black) 0%, #2a2a2a 18%, #7d7d7d 45%, var(--fade-grey) 68%, #f2f2f2 71%);
  }
  .lower-band {
    position: absolute;
    left: 0;
    top: 526px;
    width: 1200px;
    height: 215px;
    background: linear-gradient(to bottom, var(--paper-white) 0%, #f4f4f4 25%, var(--lower-grey) 100%);
  }
  .divider {
    position: absolute;
    left: 0;
    top: 526px;
    width: 1200px;
    height: 4px;
    background: var(--brand-red);
  }
  .divider-glow {
    position: absolute;
    left: 0;
    top: 520px;
    width: 1200px;
    height: 6px;
    background: var(--paper-white);
  }
  .phones {
    position: absolute;
    right: 46px;
    top: 24px;
    margin: 0;
    text-align: right;
    font-family: "Tinos", "Times New Roman", serif;
    font-weight: 700;
    font-size: 36px;
    line-height: 52px;
    color: var(--brand-red);
    text-shadow:
      -2px -2px 0 var(--paper-white), 2px -2px 0 var(--paper-white),
      -2px 2px 0 var(--paper-white), 2px 2px 0 var(--paper-white),
      0 2px 0 var(--paper-white), 0 -2px 0 var(--paper-white),
      2px 0 0 var(--paper-white), -2px 0 0 var(--paper-white);
  }
  .phones span { display: block; }
  .person {
    position: absolute;
    left: 0;
    top: 272px;
    width: 1190px;
    text-align: center;
  }
  .person-name {
    margin: 0;
    font-family: "Tinos", "Times New Roman", serif;
    font-weight: 700;
    font-size: 68px;
    line-height: 76px;
    letter-spacing: 5px;
    text-transform: uppercase;
    color: var(--brand-red);
    text-shadow:
      -1px -1px 0 var(--paper-white), 1px -1px 0 var(--paper-white),
      -1px 1px 0 var(--paper-white), 1px 1px 0 var(--paper-white),
      3px 3px 4px var(--shadow-dark);
  }
  .person-role {
    margin: 0;
    padding-left: 20px;
    font-family: "Tinos", "Times New Roman", serif;
    font-weight: 700;
    font-size: 32px;
    line-height: 36px;
    color: var(--paper-white);
    text-shadow: 2px 2px 3px var(--shadow-dark);
  }
  .address {
    position: absolute;
    left: 0;
    top: 570px;
    width: 1210px;
    margin: 0;
    text-align: center;
    font-family: "Arimo", Arial, sans-serif;
    font-weight: 700;
    font-style: normal;
    font-size: 40px;
    line-height: 53px;
    color: var(--brand-red);
    text-shadow: 2px 2px 2px var(--shadow-dark);
  }
  .address span { display: block; }
  .web, .email {
    position: absolute;
    top: 682px;
    margin: 0;
    font-family: "Tinos", "Times New Roman", serif;
    font-weight: 700;
    font-size: 34px;
    line-height: 40px;
    color: var(--deep-red);
    text-shadow: 1px 1px 2px rgba(0, 0, 0, 0.35);
  }
  .web { left: 50px; }
  .email { right: 48px; top: 688px; }
</style>
</head>
<body>
  <main class="card">
    <div class="lower-band"></div>
    <div class="divider-glow"></div>
    <div class="divider"></div>

    <p class="phones">
      <span class="phone">Phone +61 3 5550 1827</span>
      <span class="mobile">Mobile +61 455 501 936</span>
    </p>

    <section class="person">
      <h1 class="person-name">Corbin Hale</h1>
      <p class="person-role">Account Manager</p>
    </section>

    <address class="address">
      <span>Suite xxx, 214 Dawlish Parade</span>
      <span>Melbourne, Victoria 3000</span>
    </address>

    <p class="web">www.vantrelle.com.au</p>
    <p class="email">sales@vantrelle.com.au</p>
  </main>
</body>
</html>
```